Torvane Travel Business Card Design

We need a new business card design for our travel agency business - Torvane Travel. We design packages to some of the most popular travel destinations in the world for groups, individuals and also tailor-make personalised packages. Our logo attached must be used. On the back of the card we would like a list of all websites under our Torvane brand to be posted. We would like clean, modern, simple design.

Industry/Entity Type

Travel Agent

Contact Information for Business Card

Owen Pridmore
National Sales Manager
Reservations: 1300 742 689
Tel: 61 28473 5096
Fax: 61 2847 3971
Email: owen@torvanetravel.com.au
Web: www.torvanetravel.com.au

Address: Level 1, 417 Harwick Street
Sydney NSW 2000 Australia

Requirements
Must have
• On the back of the card we want all websites listed under our Torvane brand.
• Torvane Travel Group - Wholesale Specialists
• www.qpjourneys.com.au - New Caledonia
• www.bravelmijourneys.com.au - Tahiti
• www.sorvenbreakhub.com.au - China
Nice to have
• Modern, clean lined, simple and fresh
Should not have
• Look dull

```html
<!DOCTYPE html>
<html lang="en">
<head>
<meta charset="utf-8">
<title>Torvane Travel Business Card</title>
<link rel="stylesheet" href="https://fonts.googleapis.com/css2?family=Fira+Sans+Condensed:wght@400;500&family=Source+Sans+3:wght@400&display=swap">
<style>
:root{
  --bg:#a9a7a8;
  --purple:#33247a;
  --red:#dc2f2a;
  --white:#ffffff;
  --paper:#f8f8f8;
  --navy:#2c2173;
}
*{margin:0;padding:0;box-sizing:border-box}
html,body{width:1200px;height:1200px;overflow:hidden}
body{background:var(--bg);position:relative;font-family:"Source Sans 3",sans-serif}
.card{position:absolute;width:712px;height:420px;border-radius:24px;overflow:hidden}

/* back */
.card-back{left:238px;top:118px;background:var(--purple)}
.back-wordmark{position:absolute;left:0;right:0;top:106px;text-align:center;white-space:nowrap;font-family:"Fira Sans Condensed",sans-serif;font-weight:500;font-size:54px;line-height:1;color:var(--white)}
.back-tagline{position:absolute;left:0;right:0;top:194px;text-align:center;white-space:nowrap;font-size:18px;letter-spacing:10.5px;color:var(--white)}
.site-band{position:absolute;left:0;right:0;top:257px;height:107px;background:var(--red);display:flex;flex-direction:column;justify-content:center;align-items:center;color:var(--white);font-size:18px;line-height:24px}

/* front */
.card-front{left:231px;top:645px;background:var(--paper);color:var(--navy)}
.person-name{position:absolute;left:34px;top:62px;font-family:"Fira Sans Condensed",sans-serif;font-weight:500;font-size:28px;white-space:nowrap}
.person-title{position:absolute;left:34px;top:101px;font-size:17px;color:var(--red);white-space:nowrap}
.front-wordmark{position:absolute;right:48px;top:90px;white-space:nowrap;font-family:"Fira Sans Condensed",sans-serif;font-weight:500;font-size:60px;line-height:1;color:var(--navy)}
.contact-list{position:absolute;left:34px;top:213px;list-style:none;font-size:18px;line-height:24px}
.contact-list li{display:flex;align-items:center;white-space:nowrap}
.contact-list svg{width:18px;height:18px;margin-right:18px;fill:var(--red)}
.contact-list .accent{color:var(--red)}
.address{position:absolute;left:34px;top:313px;font-size:18px;line-height:27px;font-style:normal;white-space:nowrap}
.base-strip{position:absolute;left:0;bottom:0;width:420px;height:17px;background:var(--navy)}
.reservations{position:absolute;right:0;bottom:0;width:322px;height:60px;background:var(--red);clip-path:polygon(32px 0,100% 0,100% 100%,0 100%);color:var(--white);font-size:18px;display:flex;align-items:center;justify-content:flex-end;padding-right:46px;padding-bottom:2px;white-space:nowrap}
</style>
</head>
<body>

<section class="card card-back" aria-label="Business card back">
  <div class="back-wordmark">Torvane Travel Group</div>
  <div class="back-tagline">Wholesale Specialists</div>
  <div class="site-band">
    <p>New Caledonia - www.qpjourneys.com.au</p>
    <p>Tahiti - www.bravelmijourneys.com.au</p>
    <p>China - www.sorvenbreakhub.com.au</p>
  </div>
</section>

<section class="card card-front" aria-label="Business card front">
  <h1 class="person-name">Owen Pridmore</h1>
  <p class="person-title">National Sales Manager</p>
  <div class="front-wordmark">Torvane Travel</div>

  <ul class="contact-list">
    <li><svg viewBox="0 0 20 20" aria-hidden="true"><path d="M2 7c0-3 4-4 8-4s8 1 8 4l-4 1-1-2H7L6 8zM5 9h10l2 8H3z"/></svg>61 28473 5096</li>
    <li><svg viewBox="0 0 20 20" aria-hidden="true"><path d="M6 2h8v4H6zM2 7h16v7h-3v-3H5v3H2zM6 12h8v6H6z"/></svg>61 2847 3971</li>
    <li><svg viewBox="0 0 20 20" aria-hidden="true"><path d="M2 5h16v10H2zM3 6l7 5 7-5v1l-7 5-7-5z" fill-rule="evenodd"/></svg>owen@torvanetravel.com.au</li>
    <li><svg viewBox="0 0 20 20" aria-hidden="true"><g fill="none" stroke="#dc2f2a" stroke-width="1.6"><circle cx="10" cy="10" r="7.5"/><ellipse cx="10" cy="10" rx="3" ry="7.5"/><path d="M2.5 10h15"/></g></svg>www.<span class="accent">torvanetravel</span>.com.au</li>
  </ul>

  <address class="address">
    Level 1, 417 Harwick Street<br>
    Sydney NSW 2000 Australia
  </address>

  <div class="base-strip"></div>
  <div class="reservations">Reservations: 1300 742 689</div>
</section>

</body>
</html>
```